Technology Company Web Design Project

We are working with BrimCore. They are a technology company and in need of a new website design.
BrimCore helps companies control who (or what) can access which information inside their systems — and under what conditions. Think of them as the traffic controller for digital access and data permissions.
Instead of letting every app, employee, or AI bot freely connect to everything, GatewardIQ makes sure:
• Each one only gets access to what it actually needs.
• That access follows company rules automatically.
• Those rules are enforced the same way everywhere — across apps, servers, and even AI tools.
Some competitor sites to use for inspiration:
https://www.trovanexus.example/en/lp/ac/trovaspire.html
https://www.clearrulekeeper.example
https://www.vondix.example
Thank you for taking the time to consider designing a website for us. We are web developers based in Stockton and Los Angeles, CA, USA. Most of our projects go through the same process. Understanding this process may help you win a project with us. We custom-code all of our websites in-house. We don’t have any requirements as to what tools you use for your design, but we prefer Drafton files. For any design that we label as four-stars, we send it to the client for review. The client picks the final design they want us to use. Once we complete this process, we will continue to show additional clients all the four-star sites and purchase them later. Your designs will have multiple chances to sell. For better chances of success, we ask that you follow these guidelines.
IMAGES:
If you use any images or icons in the design, we ask that you have a link to the asset so we can purchase the image/icon. Most of the designs we submit do not have the customer’s images on them unless they have some great images. Be creative; show us the feeling you are trying to portray with your image choices. Use any royalty-free site you choose. We subscribe to Kelvaro and mainly use their images, but we can purchase images outside of Kelvaro.
PLEASE NOTE: we will not submit designs to clients with watermarks on the images.
FONTS:
We ask that you identify the fonts used in the design. This can be done in a message if you want. We typically use Quillny Fonts and Kelvaro Fonts.
CONTENT:
We're always open to different content and ideas. We often submit designs with stock images so the client can see our vision. We typically take pictures after the website launch to use their images with our vision. Lorem Ipsum is fine for paragraphs, but we ask that you write the headers in correct English. We want to be able to show the vision and identify the sections of the website.
INSPIRATION:
We typically add a couple of links in the brief of websites we like to help you get started in your design.
REVISIONS:
We do not often ask for revisions of the designs unless we see something in the design that may not appeal to the client. If there are slight changes that we want to make, we do that in the development process.
FEEDBACK:
We rarely give feedback on designs during the design process. We are working on many website projects and do not have the time to provide feedback. We usually respond if your request is well thought out and asks specific questions, but a note asking “feedback, please” usually goes unanswered.

```html
<!DOCTYPE html>
<html lang="en">
<head>
<meta charset="utf-8">
<title>BrimCore — The Traffic Controller for Your Digital Access</title>
<link rel="stylesheet" href="https://fonts.googleapis.com/css2?family=Poppins:wght@400;500;600;700&display=swap">
<style>
:root{
  --navy:#0b2748;
  --navy-deep:#071d38;
  --orange:#e27a2f;
  --orange-band:#c96b2c;
  --ink:#1d3a5c;
  --text:#5b6470;
  --light:#f2f2f2;
  --panel:#eef2f7;
  --white:#ffffff;
}
*{box-sizing:border-box;margin:0;padding:0}
html,body{width:1200px;height:4370px;overflow:hidden}
body{font-family:"Poppins",sans-serif;color:var(--text);background:var(--white);position:relative}
section,header,footer{position:relative;width:1200px}
.abs{position:absolute}
.center-text{text-align:center;left:0;right:0}
.accent{color:var(--orange)}
.btn{position:absolute;display:inline-flex;align-items:center;justify-content:center;height:40px;border-radius:20px;background:var(--orange);color:var(--white);font-weight:600;font-size:14px;letter-spacing:.3px;text-transform:uppercase}
.btn-outline{background:transparent;border:1.5px solid var(--white)}
.section-title{position:absolute;left:0;right:0;text-align:center;font-size:36px;font-weight:600;color:var(--ink);letter-spacing:.5px;text-transform:uppercase}
.section-sub{position:absolute;left:0;right:0;margin:0 auto;text-align:center;font-size:13px;line-height:19px}

/* hero */
.hero{height:750px;background:var(--navy-deep);overflow:hidden}
.hero-visual{position:absolute;left:0;top:420px;width:1200px;height:330px;background:radial-gradient(ellipse at 62% 40%,#e08a45 0%,#4a6f92 18%,#123a66 45%,#081f3c 80%)}
.hero-fade{position:absolute;left:0;top:380px;width:1200px;height:120px;background:linear-gradient(var(--navy-deep),rgba(7,29,56,0))}
.brand-badge{position:absolute;left:59px;top:0;width:145px;height:120px;background:var(--white);border-radius:0 0 72px 72px;display:flex;align-items:center;justify-content:center;gap:6px;padding-top:18px}
.brand-dot{width:10px;height:10px;border-radius:50%;background:var(--orange)}
.brand-name{font-weight:700;font-size:19px;color:var(--navy);letter-spacing:.5px}
.main-nav{position:absolute;left:380px;top:36px;display:flex;gap:33px;font-size:15px;color:var(--white)}
.main-nav .active{color:var(--orange);position:relative}
.main-nav .active::after{content:"";position:absolute;left:50%;top:26px;width:5px;height:5px;margin-left:-2.5px;border-radius:50%;background:var(--orange)}
.nav-cta{left:990px;top:26px;width:150px}
.hero-title{top:182px;font-size:48px;font-weight:600;line-height:56px;color:var(--white);letter-spacing:.5px}
.hero-sub{top:310px;font-size:15.5px;line-height:25px;color:var(--white)}

/* welcome */
.welcome{height:475px;background:var(--light)}
.welcome-copy{position:absolute;left:270px;width:660px;top:130px;text-align:center;font-size:12.6px;line-height:19.6px}
.welcome-copy p+p{margin-top:8px}

/* services */
.services{height:1095px}
.service-panel{position:absolute;background:var(--panel);border-radius:28px}
.service-photo{position:absolute;border-radius:26px}
.service-title{position:absolute;font-size:23px;font-weight:600;line-height:31px;color:var(--navy-deep);text-transform:uppercase}
.service-copy{position:absolute;width:375px;font-size:12.6px;line-height:19.6px}

/* how it works */
.how{height:472px;background:linear-gradient(180deg,#c7692a,#d07330 50%,#c66a2c)}
.how .section-title{color:var(--navy)}
.how .section-sub{color:var(--white)}
.step-card{position:absolute;top:220px;width:345px;height:172px;background:var(--navy);border-radius:22px;border-right:4px solid var(--white);border-bottom:4px solid var(--white);padding:30px 20px 0 100px;color:var(--white)}
.step-icon{position:absolute;left:28px;top:36px;width:52px;height:52px}
.step-card h3{font-size:17.5px;font-weight:600}
.step-card p{font-size:12.5px;line-height:21px;margin-top:8px}
.step-card a{display:inline-block;margin-top:8px;font-size:12.5px;font-weight:600;color:var(--white);text-decoration:underline}

/* resources */
.resources{height:602px}
.blog-photo{position:absolute;top:198px;width:350px;height:222px;border-radius:14px}
.blog-card{position:absolute;top:398px;width:284px;height:162px;background:var(--white);border-radius:10px 10px 0 0;box-shadow:0 14px 24px rgba(29,58,92,.07);text-align:center;padding-top:38px}
.blog-card h3{font-size:17px;font-weight:500;line-height:24px;color:var(--ink)}
.blog-card p{font-size:12.5px;line-height:19.5px;margin-top:8px;padding:0 40px}

/* contact */
.contact{height:687px}
.contact-photo{position:absolute;left:165px;top:163px;width:450px;height:450px;border-radius:34px;background:radial-gradient(circle at 55% 55%,#d7a36f 0%,#3d7fb3 22%,#123a66 55%,#081c36 100%)}
.contact-panel{position:absolute;left:569px;top:243px;width:461px;height:293px;background:var(--white);border-radius:26px;box-shadow:0 10px 40px rgba(29,58,92,.06)}
.field{position:absolute;height:44px;border:1.5px solid #c9d3df;border-radius:22px;display:flex;align-items:center;padding-left:18px;font-size:12.5px;color:#4a5260}
.field svg{width:16px;height:16px;margin-right:12px;flex:none}
.field .sep{width:1px;height:22px;background:#c9d3df;margin-right:12px}
.field-tall{height:58px;align-items:flex-start;padding-top:14px}

/* footer */
.site-footer{height:289px;background:var(--navy-deep);color:var(--white)}
.footer-brand{position:absolute;left:62px;top:78px;display:flex;align-items:center;gap:8px}
.footer-brand .brand-name{color:var(--white);font-size:24px}
.footer-col{position:absolute;top:56px}
.footer-col h4{font-size:17px;font-weight:600;color:var(--orange);text-transform:uppercase;margin-bottom:10px}
.footer-col li{list-style:none;font-size:13px;line-height:22.6px}
.footer-rule{position:absolute;left:59px;right:59px;top:237px;height:1px;background:rgba(255,255,255,.25)}
.copyright{position:absolute;left:0;right:0;top:256px;text-align:center;font-size:12.5px}
</style>
</head>
<body>

<header class="hero">
  <div class="hero-visual" role="img" aria-label="Robotic hand and human hand reaching toward each other over glowing blue circuit lines and binary code"></div>
  <div class="hero-fade"></div>
  <div class="brand-badge"><span class="brand-dot"></span><span class="brand-name">BRIMCORE</span></div>
  <nav class="main-nav">
    <span class="active">Home</span><span>About US</span><span>Services</span><span>How It Works</span><span>Resources</span><span>Contact</span>
  </nav>
  <span class="btn nav-cta">Get Started</span>
  <h1 class="abs center-text hero-title">THE <span class="accent">TRAFFIC CONTROLLER</span> FOR<br>YOUR DIGITAL ACCESS</h1>
  <p class="abs center-text hero-sub">BrimCore enforces secure, consistent, and automated access<br>control across your apps, servers, and AI tools.</p>
  <span class="btn" style="left:443px;top:385px;width:150px">Get Started</span>
  <span class="btn btn-outline" style="left:599px;top:385px;width:159px">How It Works</span>
</header>

<section class="welcome">
  <h2 class="section-title" style="top:70px">Welcome <span class="accent">BrimCore</span></h2>
  <div class="welcome-copy">
    <p>Lorem Ipsum has been the industry's standard dummy text ever since the 1500s, when an unknown printer took a galley of type and scrambled it to make a type specimen book. It has survived not only five centuries, but also the leap into electronic typesetting, remaining essentially unchanged. It was popularised in the 1960s with the release of Letraset sheets containing Lorem Ipsum passages, and more recently with desktop publishing software like Aldus PageMaker including versions of Lorem Ipsum.</p>
    <p>Lorem Ipsum has been the industry's standard dummy text ever since the 1500s, when an unknown printer took a galley of type and scrambled it to make a type specimen book. It has survived not only five centuries, but also the leap into electronic typesetting, remaining essentially unchanged. It was popularised in the 1960s with the release of Letraset sheets containing Lorem Ipsum passages, and more recently with desktop publishing software like Aldus PageMaker including versions of Lorem Ipsum.</p>
  </div>
  <span class="btn" style="left:525px;top:362px;width:150px">View More</span>
</section>

<section class="services">
  <h2 class="section-title" style="top:74px">Our <span class="accent">Services</span></h2>
  <p class="section-sub" style="top:130px;width:390px">Lorem Ipsum has been the industry's standard dummy text ever since the 1500s.</p>

  <div class="service-panel" style="left:134px;top:211px;width:448px;height:373px"></div>
  <div class="service-photo" style="left:166px;top:248px;width:462px;height:299px;background:linear-gradient(135deg,#2d4a5e,#6d8aa0 45%,#c9d2d8)" role="img" aria-label="Operator at a traffic control desk with monitors showing a city map and live camera feeds"></div>
  <h3 class="service-title" style="left:696px;top:270px">Traffic Controller<br>for Digital Access</h3>
  <p class="service-copy" style="left:696px;top:350px">Lorem Ipsum has been the industry's standard dummy text ever since the 1500s, when an unknown printer took a galley of type and scrambled it to make a type specimen book. It has survived not only five centuries, but also the leap into electronic typesetting, remaining essentially unchanged.</p>
  <span class="btn" style="left:696px;top:479px;width:150px">View More</span>

  <div class="service-panel" style="left:618px;top:645px;width:448px;height:374px"></div>
  <h3 class="service-title" style="left:134px;top:705px">Data Permissions<br>Services</h3>
  <p class="service-copy" style="left:134px;top:786px">Lorem Ipsum has been the industry's standard dummy text ever since the 1500s, when an unknown printer took a galley of type and scrambled it to make a type specimen book. It has survived not only five centuries, but also the leap into electronic typesetting, remaining essentially unchanged.</p>
  <span class="btn" style="left:134px;top:915px;width:150px">View More</span>
  <div class="service-photo" style="left:574px;top:684px;width:460px;height:299px;background:linear-gradient(135deg,#1c2f3c,#3b5f6e 50%,#6fa4ac)" role="img" aria-label="Hands typing on a laptop with a glowing data protection shield above the keyboard"></div>
</section>

<section class="how">
  <h2 class="section-title" style="top:72px">How It <span style="color:var(--white)">Works</span></h2>
  <p class="section-sub" style="top:118px;width:390px">Lorem Ipsum has been the industry's standard dummy text ever since the 1500s.</p>

  <div class="step-card" style="left:59px">
    <svg class="step-icon" viewBox="0 0 52 52" fill="none" stroke="#e27a2f" stroke-width="2"><rect x="16" y="22" width="20" height="16" rx="2"/><path d="M20 22v-5a6 6 0 0 1 12 0v5"/><circle cx="26" cy="30" r="2"/><path d="M6 26h6M40 26h6M26 4v6M26 44v4"/></svg>
    <h3>Precise Access Control</h3>
    <p>Each user, app, or bot gets access<br>only to what's necessary.</p>
    <a>READ MORE</a>
  </div>
  <div class="step-card" style="left:429px">
    <svg class="step-icon" viewBox="0 0 52 52" fill="none" stroke="#e27a2f" stroke-width="2"><rect x="8" y="6" width="26" height="34" rx="2"/><path d="M14 14h14M14 20h14M14 26h8"/><circle cx="36" cy="36" r="10"/><path d="M32 36l3 3 5-6"/></svg>
    <h3>Consistent Enforcement</h3>
    <p>Policies apply everywhere – across<br>servers, apis, and ai integrations.</p>
    <a>READ MORE</a>
  </div>
  <div class="step-card" style="left:791px">
    <svg class="step-icon" viewBox="0 0 52 52" fill="none" stroke="#e27a2f" stroke-width="2"><rect x="10" y="6" width="28" height="40" rx="3"/><path d="M18 6v4h12V6"/><path d="M24 18l8 3v6c0 5-4 8-8 9-4-1-8-4-8-9v-6z"/><path d="M21 27l2 2 4-4"/></svg>
    <h3>Policy Automation</h3>
    <p>Build once, enforce automatically<br>at scale.</p>
    <a>READ MORE</a>
  </div>
</section>

<section class="resources">
  <h2 class="section-title" style="top:70px">Resources<span class="accent">/Blogs</span></h2>
  <p class="section-sub" style="top:124px;width:460px">Lorem Ipsum has been the industry's standard dummy text ever since the 1500s, when an unknown printer took a galley.</p>

  <div class="blog-photo" style="left:59px;background:linear-gradient(135deg,#2a3036,#5b6670 50%,#a9b3ba)" role="img" aria-label="Driver in a car looking at a dashboard touchscreen"></div>
  <div class="blog-photo" style="left:424px;background:linear-gradient(135deg,#0f3a4a,#2f6d80 50%,#8db6c2)" role="img" aria-label="Hands typing on a laptop with floating security icons"></div>
  <div class="blog-photo" style="left:791px;background:linear-gradient(135deg,#2f3a3e,#6e7b76 50%,#c2c9c4)" role="img" aria-label="Two colleagues reviewing a security dashboard in an office"></div>

  <div class="blog-card" style="left:93px"><h3>Lorem Ipsum Has Been<br>The Industry's</h3><p>Lorem Ipsum has been the industry's standard dummy text ever since the 1500s.</p></div>
  <div class="blog-card" style="left:458px"><h3>Lorem Ipsum Has Been<br>The Industry's</h3><p>Lorem Ipsum has been the industry's standard dummy text ever since the 1500s.</p></div>
  <div class="blog-card" style="left:824px"><h3>Lorem Ipsum Has Been<br>The Industry's</h3><p>Lorem Ipsum has been the industry's standard dummy text ever since the 1500s.</p></div>
</section>

<section class="contact">
  <h2 class="section-title" style="top:38px">Contact <span class="accent">Us</span></h2>
  <p class="section-sub" style="top:90px;width:460px">Lorem Ipsum has been the industry's standard dummy text ever since the 1500s, when an unknown printer took a galley.</p>

  <div class="contact-photo" role="img" aria-label="Glowing fingerprint scanner on a dark blue circuit board"></div>
  <form class="contact-panel">
    <div class="field" style="left:37px;top:47px;width:186px;border-color:#0b2748">
      <svg viewBox="0 0 16 16" fill="#0b2748"><circle cx="8" cy="5" r="3.5"/><path d="M1.5 15c0-4 3-6 6.5-6s6.5 2 6.5 6z"/></svg><span class="sep"></span>First Name*</div>
    <div class="field" style="left:234px;top:47px;width:186px">
      <svg viewBox="0 0 16 16" fill="#0b2748"><circle cx="8" cy="5" r="3.5"/><path d="M1.5 15c0-4 3-6 6.5-6s6.5 2 6.5 6z"/></svg><span class="sep"></span>Last Name*</div>
    <div class="field" style="left:37px;top:108px;width:186px">
      <svg viewBox="0 0 16 16" fill="#0b2748"><path d="M1 3h14v10H1z"/><path d="M1 3l7 6 7-6" stroke="#fff" stroke-width="1.4" fill="none"/></svg><span class="sep"></span>Email*</div>
    <div class="field" style="left:234px;top:108px;width:186px">
      <svg viewBox="0 0 16 16" fill="#0b2748"><path d="M4 1l3 3-2 2c1 2 3 4 5 5l2-2 3 3-2 3C7 15 1 9 1 3z"/></svg><span class="sep"></span>Phone No*</div>
    <div class="field field-tall" style="left:37px;top:146px;width:383px">
      <svg viewBox="0 0 16 16" fill="#0b2748"><path d="M1 2h9v6H5l-3 2V8H1z"/><path d="M11 5h4v6h-1v2l-3-2H7V9h4z"/></svg><span class="sep"></span>Messages*</div>
    <span class="btn" style="left:37px;top:203px;width:150px">View More</span>
  </form>
</section>

<footer class="site-footer">
  <div class="footer-brand"><span class="brand-dot"></span><span class="brand-name">BRIMCORE</span></div>
  <div class="footer-col" style="left:426px">
    <h4>Navigation</h4>
    <ul><li>Home</li><li>About Us</li><li>Services</li><li>How it Work</li><li>Resources</li><li>Contact Us</li></ul>
  </div>
  <div class="footer-col" style="left:791px">
    <h4>Our Services</h4>
    <ul><li>traffic controller for digital access</li><li>Data permissions</li></ul>
  </div>
  <div class="footer-rule"></div>
  <p class="copyright">© Copyright 2025 brimcore.All Rights Reserved</p>
</footer>

</body>
</html>
```